Meadowbrook Fellowship Chapel Banner Design

Designing 6 banners (3 + 3 that will hang on opposite sides of our auditorium) that are 10 feet long by 4 feet wide.

Use our branding guide - specifically item 4 (vertical logo) and item 5 (icon logo).

Design elements found in our AWAKE booklet, we would like to see designs that utilize the white, green and blue colour palettes but NOT the grey. Other colours may be incorporated (e.g. coral).

We are looking for 3 banner designs that would match on either side of the auditorium, the first banner incorporating the word "TRUTH", the second incorporating the word "LOVE", and the third incorporating the word "MISSION".

We interested in incorporating graphics such as trees or outdoor themes.

Font styles to use
Other font styles liked:
• Montserrat

Colors
34a7d7
00a990
f47c35

Requirements
Must have
• Banner Type #1 include the word "TRUTH"
Banner Type #2 include the word "LOVE"
Banner Type #3 include the word "MISSION"

Colour scheme must include CMYK 54 / 5 / 16 / 0 (which is available in the branding guide.) We have selected the three colours, included below in the brief.

From the branding guide - utilize #5 (icon) for the banner.

UPDATE: After reviewing the initial submissions, we are asking for designs that ONLY incorporate #5 - the ICON logo for the banners.
Nice to have
• It would be nice to have some creativity with the colour ... though a more minimalistic style is preferred.

Graphic adaptations such as trees in the background would be of interest.
Should not have
• Colour scheme should not be gray scale.

The banners should NOT be too busy.

Scripture verses (written out) are not necessary.

```html
<!DOCTYPE html>
<html lang="en">
<head>
<meta charset="utf-8">
<title>Meadowbrook Fellowship Chapel – Auditorium Banners</title>
<link href="https://fonts.googleapis.com/css2?family=Montserrat:wght@700;900&display=swap" rel="stylesheet">
<style>
  :root {
    --stage: #5b5b5b;
    --sky-blue: #2aa8dc;
    --brand-blue: #34a7d7;
    --brand-teal: #00a990;
    --teal-mid: #15ac98;
    --teal-deep: #0fae94;
    --brand-coral: #f47c35;
    --sand: #c8ad72;
    --leaf: #1aa86a;
    --bark: #3f4a35;
    --white: #ffffff;
    --word-shadow: rgba(150, 225, 215, 0.85);
  }
  * { box-sizing: border-box; margin: 0; padding: 0; }
  html, body {
    width: 1200px; height: 996px; overflow: hidden;
    background: var(--stage);
    font-family: "Montserrat", Arial, sans-serif;
  }
  .banner-set { position: relative; width: 1200px; height: 996px; }
  .banner {
    position: absolute; top: 37px; width: 369px; height: 923px;
    overflow: hidden; border: 1px solid #777;
  }
  .banner--love    { left: 33px;  background: linear-gradient(180deg, var(--sky-blue) 0%, #1aa9b6 35%, var(--teal-mid) 60%, var(--teal-deep) 100%); }
  .banner--truth   { left: 417px; border-color: #111;
                     background: linear-gradient(180deg, #1aac98 0%, #22a9b8 25%, var(--brand-blue) 45%, var(--brand-blue) 60%, var(--teal-mid) 70%, var(--teal-deep) 100%); }
  .banner--mission { left: 800px; background: linear-gradient(180deg, var(--brand-coral) 0%, #e4a25a 14%, var(--sand) 26%, #84a583 38%, var(--teal-mid) 48%, var(--teal-deep) 100%); }

  .forest-scene {
    position: absolute; left: 0; right: 0; top: 345px; bottom: 0;
    background:
      radial-gradient(ellipse 60% 45% at 24% 18%, rgba(20, 170, 140, 0.85), transparent 70%),
      radial-gradient(ellipse 55% 40% at 88% 40%, rgba(26, 168, 106, 0.7), transparent 70%),
      linear-gradient(180deg, rgba(20, 172, 150, 0.55) 0%, rgba(15, 174, 148, 0.6) 60%, rgba(63, 74, 53, 0.35) 100%);
  }

  .brand-mark {
    position: absolute; top: 88px; left: 0; right: 0;
    text-align: center; color: var(--white);
    font-weight: 700; font-size: 19px; line-height: 1.25; letter-spacing: 0.08em;
  }
  .brand-mark__name { display: block; }

  .banner-word {
    position: absolute; left: 50%; top: 892px;
    transform-origin: 0 0;
    transform: rotate(-90deg) translateY(-50%);
    white-space: nowrap;
    color: var(--white);
    font-weight: 900; font-size: 128px; line-height: 0.78;
    letter-spacing: 0.01em;
    text-shadow: 6px 6px 0 var(--word-shadow);
  }
  .banner--mission .banner-word { font-size: 126px; }
</style>
</head>
<body>
  <main class="banner-set">
    <section class="banner banner--love">
      <div class="forest-scene" role="img" aria-label="Illustrated green hills with bare brown trees in the foreground"></div>
      <div class="brand-mark"><span class="brand-mark__name">MEADOWBROOK</span><span class="brand-mark__name">FELLOWSHIP CHAPEL</span></div>
      <h2 class="banner-word">LOVE</h2>
    </section>

    <section class="banner banner--truth">
      <div class="forest-scene" role="img" aria-label="Illustrated green hills with bare brown trees in the foreground"></div>
      <div class="brand-mark"><span class="brand-mark__name">MEADOWBROOK</span><span class="brand-mark__name">FELLOWSHIP CHAPEL</span></div>
      <h2 class="banner-word">TRUTH</h2>
    </section>

    <section class="banner banner--mission">
      <div class="forest-scene" role="img" aria-label="Illustrated green hills with bare brown trees in the foreground"></div>
      <div class="brand-mark"><span class="brand-mark__name">MEADOWBROOK</span><span class="brand-mark__name">FELLOWSHIP CHAPEL</span></div>
      <h2 class="banner-word">MISSION</h2>
    </section>
  </main>
</body>
</html>
```